依頼詳細
タワーマンションの理事長にチラシを配布しようと思っています。そのチラシデザイン制作をお願いします。見る人が思わず参加したくなるようなインパクトのあるデザインをお願いします。
記載項目
社名:株式会社MN建築設計/電話:06-4827-3956/URL:http://mn-kenchiku.co.jp
サイズ
A4
ページ数
両面
希望イメージ
シンプル 複雑
単色 カラフル
暗い 明るい
日常 高級
遊び心 厳粛
未来的 伝統的
女性的 男性的

弊社のイメージカラーに合っていたこと、内容が見やすくて分かりやすかった為

このたびは短い期間でありながらもご参加いただきありがとうございました。
皆様の提案は全て良かったので選定に苦慮いたしました。今回選定されなかったご提案者様は残念な結果となりましたが、今後もご提案をお願いするときには是非参加くださいますようお願い申し上げます。

```html
<!DOCTYPE html>
<html lang="ja">
<head>
<meta charset="utf-8">
<title>タワーマンション管理組合 交流会</title>
<link href="https://fonts.googleapis.com/css2?family=Noto+Sans+JP:wght@400;500;700;900&display=swap" rel="stylesheet">
<style>
:root{
  --sky-top:#e3f3f2;
  --sky-bottom:#cbe7e6;
  --navy:#1f3550;
  --teal:#3b9c9d;
  --teal-dark:#2c8485;
  --yellow:#f4e21a;
  --red:#d83a3a;
  --white:#ffffff;
  --grey:#8c9aa3;
  --ink:#25323d;
}
*{margin:0;padding:0;box-sizing:border-box}
html,body{width:848px;height:1200px;overflow:hidden}
body{font-family:"Noto Sans JP",sans-serif;color:var(--navy);background:var(--white)}
.flyer{position:relative;width:848px;height:1200px;overflow:hidden;background:linear-gradient(var(--sky-top),var(--sky-bottom) 60%)}
.abs{position:absolute}
.organizer-pill{left:196px;top:22px;width:412px;height:42px;border-radius:21px;background:var(--white);border:3px solid var(--navy);color:var(--navy);font-weight:700;font-size:24px;display:flex;align-items:center;justify-content:center;letter-spacing:1px}
.title{left:100px;top:58px;font-size:158px;font-weight:900;letter-spacing:6px;line-height:1;color:var(--navy)}
.badge{left:622px;top:50px;width:212px;height:212px;border-radius:50%;background:var(--yellow);display:flex;align-items:center;justify-content:center;text-align:center;font-weight:900;font-size:31px;line-height:1.3;color:var(--navy);transform:rotate(-6deg)}
.event-date{left:100px;top:222px;font-size:132px;font-weight:900;line-height:1;letter-spacing:-2px;display:flex;align-items:flex-end}
.weekday{display:inline-flex;width:48px;height:48px;border-radius:50%;background:var(--navy);color:var(--white);font-size:28px;align-items:center;justify-content:center;margin:0 0 14px 8px;letter-spacing:0}
.deadline{left:452px;top:244px;font-weight:900}
.deadline .label{font-size:28px;display:block}
.deadline .date{font-size:64px;line-height:1.05;display:flex;align-items:flex-end}
.deadline .weekday{width:34px;height:34px;font-size:20px;margin-bottom:10px}
.time{left:100px;top:352px;font-size:46px;font-weight:900;letter-spacing:1px}
.apply-box{left:398px;top:360px;width:200px;height:60px;background:var(--navy);color:var(--white);font-weight:700;font-size:20px;line-height:1.3;display:flex;align-items:center;justify-content:center;text-align:center;padding:4px 10px}
.info{left:100px;top:420px;font-weight:900}
.info-row{display:flex;align-items:center;gap:12px;margin-bottom:6px}
.tag{background:var(--teal);color:var(--white);font-size:18px;padding:2px 10px;font-weight:700}
.info-row .val{font-size:30px}
.address{font-size:15px;font-weight:500;margin-left:80px}
.skyline{left:0;top:500px;width:848px;height:270px;background:linear-gradient(rgba(140,154,163,0),rgba(140,154,163,.8) 45%,#6f7e88)}
.worries{left:0;top:765px;width:848px;height:395px;background:var(--teal)}
.worries-pill{left:150px;top:790px;width:548px;height:50px;border-radius:25px;background:var(--white);color:var(--navy);font-size:27px;font-weight:900;display:flex;align-items:center;justify-content:center}
.checklist{left:80px;top:858px;width:688px;display:grid;grid-template-columns:1fr 1fr;gap:10px 30px;list-style:none}
.checklist li{background:var(--white);height:34px;display:flex;align-items:center;gap:10px;padding-left:8px;font-size:19px;font-weight:700;color:var(--ink);white-space:nowrap;overflow:hidden}
.checklist svg{flex:none}
.program{left:60px;top:995px;width:728px;display:grid;grid-template-columns:1fr 1fr 1.1fr;gap:14px}
.session{background:var(--white);height:124px;padding:10px 12px;color:var(--ink)}
.session-head{display:flex;align-items:center;gap:8px;font-weight:900;font-size:20px}
.part{background:var(--navy);color:var(--white);font-size:13px;padding:2px 6px}
.session-title{font-size:14px;font-weight:700;margin:4px 0 2px}
.session-text{font-size:11px;line-height:1.5}
.lecturer{font-size:14px;font-weight:700;margin-top:4px}
.lecturer strong{font-size:22px;font-weight:900;margin:0 4px}
.lecturer small{font-size:10px;font-weight:500}
.notice{border:2px solid var(--white);background:var(--teal-dark);color:var(--white);height:124px;padding:8px 10px}
.notice h3{font-size:13px;font-weight:700;margin-bottom:4px}
.notice p{font-size:10.5px;line-height:1.55}
.footer{left:0;top:1160px;width:848px;height:40px;background:var(--white);color:var(--navy);font-weight:700;font-size:20px;display:flex;align-items:center;justify-content:center}
</style>
</head>
<body>
<main class="flyer">
  <div class="abs skyline" role="img" aria-label="高層マンションが建ち並ぶ街並みのイラスト"></div>

  <div class="abs organizer-pill">タワーマンション管理組合</div>
  <h1 class="abs title">交流会</h1>
  <div class="abs badge">管理組合<br>の自立を<br>目指す!</div>

  <div class="abs event-date">7/31<span class="weekday">日</span></div>
  <div class="abs deadline"><span class="label">申込締切</span><span class="date">7/19<span class="weekday">日</span></span></div>

  <div class="abs time">10:00~12:00</div>
  <div class="abs apply-box">お申し込みは<br>裏面FAXにて</div>

  <div class="abs info">
    <div class="info-row"><span class="tag">定員</span><span class="val">先着15名様</span></div>
    <div class="info-row"><span class="tag">会場</span><span class="val">ソレイユタワー天王寺</span></div>
    <div class="address">大阪府大阪市阿倍野区旭野町3-8-14</div>
  </div>

  <section class="abs worries"></section>
  <div class="abs worries-pill">マンションのこんなお悩みありませんか?</div>
  <ul class="abs checklist">
    <li><svg width="24" height="24" viewBox="0 0 24 24"><rect x="1" y="4" width="18" height="18" fill="none" stroke="#25323d" stroke-width="2"/><path d="M5 12l5 5L22 3" fill="none" stroke="#d83a3a" stroke-width="3.5"/></svg>分譲マンションの未来を考える</li>
    <li><svg width="24" height="24" viewBox="0 0 24 24"><rect x="1" y="4" width="18" height="18" fill="none" stroke="#25323d" stroke-width="2"/><path d="M5 12l5 5L22 3" fill="none" stroke="#d83a3a" stroke-width="3.5"/></svg>他のマンションはどう?</li>
    <li><svg width="24" height="24" viewBox="0 0 24 24"><rect x="1" y="4" width="18" height="18" fill="none" stroke="#25323d" stroke-width="2"/><path d="M5 12l5 5L22 3" fill="none" stroke="#d83a3a" stroke-width="3.5"/></svg>管理費の値上げ?</li>
    <li><svg width="24" height="24" viewBox="0 0 24 24"><rect x="1" y="4" width="18" height="18" fill="none" stroke="#25323d" stroke-width="2"/><path d="M5 12l5 5L22 3" fill="none" stroke="#d83a3a" stroke-width="3.5"/></svg>修繕費が高い</li>
    <li><svg width="24" height="24" viewBox="0 0 24 24"><rect x="1" y="4" width="18" height="18" fill="none" stroke="#25323d" stroke-width="2"/><path d="M5 12l5 5L22 3" fill="none" stroke="#d83a3a" stroke-width="3.5"/></svg>理事のなり手がいない</li>
    <li><svg width="24" height="24" viewBox="0 0 24 24"><rect x="1" y="4" width="18" height="18" fill="none" stroke="#25323d" stroke-width="2"/><path d="M5 12l5 5L22 3" fill="none" stroke="#d83a3a" stroke-width="3.5"/></svg>民泊問題</li>
  </ul>

  <div class="abs program">
    <article class="session">
      <div class="session-head"><span class="part">第1部</span>10:00-10:50</div>
      <p class="session-title">意見交流会(全員参加型)</p>
      <p class="session-text">参加者の方々で、運営の課題や工夫を共有し、解決策を一緒に考えます。</p>
    </article>
    <article class="session">
      <div class="session-head"><span class="part">第2部</span>11:00-11:50</div>
      <p class="session-title">修繕工事の進め方と考え方</p>
      <p class="lecturer">講師<strong>三輪 聡</strong><small>(一級建築士)</small></p>
    </article>
    <article class="notice">
      <h3>新型コロナウイルス対策について</h3>
      <p>会場では手指の消毒、マスクの着用、換気の徹底をお願いしております。当日体調のすぐれない方はご参加をお控えください。ご理解とご協力をお願いいたします。</p>
    </article>
  </div>

  <footer class="abs footer">主催：タワーマンション管理組合</footer>
</main>
</body>
</html>
```